1300 Cratelofn Van wrap

We are forklift mechanics.
Design a simple wrap to suit our 4 vans with our logo.
Add some colour/design using the base colours happy to add other colours as suits and highlights/shadows to balance/break up the white but not over power it.
Include mobile number 0491 570 266

```html
<!DOCTYPE html>
<html lang="en">
<head>
<meta charset="utf-8">
<title>1300 Cratelofn – Van Wrap</title>
<link rel="stylesheet" href="https://fonts.googleapis.com/css2?family=Anton&family=Oswald:wght@600&display=swap">
<style>
  :root {
    --backdrop: #4a4a4a;
    --wrap-white: #f4f4f4;
    --brand-red: #d0191f;
    --deep-red: #a80d12;
    --rear-grey: #55585c;
    --ink: #111111;
    --text-light: #ffffff;
  }
  html, body {
    margin: 0;
    padding: 0;
    width: 1200px;
    height: 603px;
    overflow: hidden;
    background: var(--backdrop);
  }
  .canvas {
    position: relative;
    width: 1200px;
    height: 603px;
  }
  .wrap-art {
    position: absolute;
    left: 0;
    top: 0;
  }
  .wordmark {
    font-family: "Anton", "Oswald", sans-serif;
    font-size: 56px;
    fill: var(--ink);
    letter-spacing: 0.5px;
  }
  .services {
    font-family: "Oswald", sans-serif;
    font-weight: 600;
    font-size: 21px;
    fill: var(--ink);
  }
  .phone-number {
    font-family: "Oswald", sans-serif;
    font-weight: 600;
    font-size: 34px;
    fill: var(--text-light);
  }
  .company-name {
    font-family: "Oswald", sans-serif;
    font-weight: 600;
    font-size: 17px;
    fill: var(--text-light);
  }
</style>
</head>
<body>
<main class="canvas">
  <svg class="wrap-art" width="1200" height="603" viewBox="0 0 1200 603" aria-label="1300 Cratelofn van side wrap">
    <!-- wrap base -->
    <rect class="wrap-base" x="110" y="140" width="980" height="326" rx="18" fill="var(--wrap-white)"/>

    <!-- rear grey section -->
    <path class="rear-panel" d="M1065 140 H1072 Q1090 140 1090 158 V448 Q1090 466 1072 466 H850 Z" fill="var(--rear-grey)"/>

    <!-- upper red diagonal band -->
    <polygon class="upper-band" points="876,140 1065,140 980,269 792,269" fill="var(--brand-red)"/>

    <!-- equipment illustration area -->
    <rect class="equipment-area" x="950" y="293" width="104" height="103" fill="#6a6d71" role="img" aria-label="Forklift illustration"/>

    <!-- lower red stripe and rule -->
    <polygon class="lower-stripe" points="527,342 564,342 440,466 403,466" fill="var(--deep-red)"/>
    <rect class="red-rule" x="550" y="342" width="140" height="11" fill="var(--deep-red)"/>

    <!-- phone band -->
    <polygon class="phone-band" points="531,391 813,391 813,433 492,433" fill="var(--ink)"/>
    <polygon class="base-band" points="643,436 813,436 813,464 613,464" fill="var(--deep-red)"/>

    <!-- brand wordmark -->
    <text class="wordmark" x="568" y="350">1300 CRATELOFN</text>

    <!-- services line -->
    <text class="services" x="578" y="381">HIRE - SALES - SERVICE - REPAIRS</text>

    <!-- phone icon and number -->
    <g class="phone-icon" transform="translate(585 405)">
      <circle cx="10" cy="10" r="9" fill="none" stroke="var(--text-light)" stroke-width="2"/>
      <path d="M6 5.5 L8.5 5 L9.5 8 L8 9 Q9 11.5 11 12 L12 10.5 L15 11.5 L14.5 14 Q9 15 6 5.5 Z" fill="var(--text-light)"/>
    </g>
    <text class="phone-number" x="610" y="427">0491 570 266</text>

    <!-- company name -->
    <text class="company-name">
      <tspan x="900" y="207">RIDGELINE</tspan>
      <tspan x="900" y="228">LIFT</tspan>
      <tspan x="900" y="249">SERVICE P/L</tspan>
    </text>
  </svg>
</main>
</body>
</html>
```